Brightmoor Paving Stationery Design COMMITTED PAY

We need you to design stationary for a new Business called Brightmoor Paving. We have already got the logo designed and it is attached. Obviously we're looking for a stationery set designed around the colours and style to match the logo.

Use generic name, address, phone, fax, email etc ... I will edit text to required details.

What we need:
- Business Card Design Double Sided (90 x 55m + Bleed 3mm+)
- A4 Letter head Design
- A4 Presentation Folder Design
- Invoice Header Approx 210 x 55mm (Include Logo & Images)

And whatever other bonuses you'd like to kick in associated with the package.

I've attached some images and I've got hundreds more. If you want something else in the way of images, let me know.

I look forward to your seeing your designs.
Updates

Thought I should just clarify the follwoing:

1. The Invoice Header is just a branding for the top of my accounting package form.  It is not contain any contact information or the like.  Just logo, some images and some of your creativity and flair to bring it together.
2. The business does synthetic grass (75% of the business), Wetpour Rubber Surfaces, Softfall Surfaces and Rubber Wood Mulch.  These are categories you might choose to somehow highlight on the letterhead.
3. Business Card reverse side should be used to highlight the categories using images provided.

Wow, I've had some really nice designs submitted thus far, but my concern is that I can't just have an awesome looking card.  I really feel that my card needs to either show or say what we do.  Please make sure your design either shows or says the following:

- Synthetic Grass
- Wetpour Rubber Surfaces
- Softfall Surfaces
- Rubber Wood Mulch
- Shade Structures
- Landscape Structures

Just another note, don't know if I mentioned it or not in the original brief, but I prefer the use of icons instead of text for phone, email, fax etc labels.

Industry/Entity Type

Business

Requirements
Must have
• - Provide full editable source files
- Provide letterhead in MS Word format as well
- All designs must be awesome, but also show or say what we do. This is very important to me. I want anyone to look at our letterhead, business card etc and know instantly what it is that we do.
- Super quick turnaround on handover. I need card files to the printer on Monday morning (that's my Monday at GMT+10)
Nice to have
• - Creative use of the logo for a little bit of wow
Should not have
• - not square, boxy or rigid ... Loosen up a bit!

```html
<!DOCTYPE html>
<html lang="en">
<head>
<meta charset="utf-8">
<title>Brightmoor Paving – Business Card</title>
<link href="https://fonts.googleapis.com/css2?family=Exo+2:wght@400;500;600;700&display=swap" rel="stylesheet">
<style>
  :root {
    --backdrop: #2b2b2b;
    --card-dark: #232323;
    --leaf-green: #7dc242;
    --leaf-green-deep: #5fa82c;
    --sky-blue: #29a8e0;
    --ink-white: #ffffff;
  }
  * { margin: 0; padding: 0; box-sizing: border-box; }
  html, body { width: 1200px; height: 900px; overflow: hidden; }
  body {
    background: var(--backdrop);
    font-family: "Exo 2", "Segoe UI", sans-serif;
    position: relative;
  }
  .card {
    position: absolute;
    width: 540px;
    height: 330px;
    overflow: hidden;
    box-shadow: 0 18px 40px rgba(0,0,0,.55);
  }

  /* Reverse side */
  .card-reverse { left: 90px; top: 100px; background: var(--card-dark); }
  .reverse-brand {
    position: absolute; left: 0; right: 0; top: 92px;
    display: flex; align-items: center; justify-content: center; gap: 14px;
  }
  .brand-dot { width: 34px; height: 34px; border-radius: 50%; background: var(--sky-blue); }
  .reverse-name {
    color: var(--leaf-green); font-weight: 700; font-size: 34px;
    letter-spacing: 1px; text-transform: uppercase;
  }
  .reverse-tagline {
    position: absolute; left: 0; right: 0; top: 146px; text-align: center;
    color: var(--sky-blue); font-weight: 600; font-size: 13px;
  }
  .service-list {
    position: absolute; left: 30px; right: 30px; bottom: 46px;
    text-align: center; font-size: 14px; line-height: 1.6; font-weight: 500;
  }
  .service-blue { color: var(--sky-blue); }
  .service-green { color: var(--leaf-green); }
  .service-sep { color: #9a9a9a; margin: 0 4px; }

  /* Front side */
  .card-front { left: 570px; top: 470px; background: var(--card-dark); }
  .front-split { position: absolute; inset: 0; }
  .contact-block {
    position: absolute; right: 26px; top: 24px; text-align: right;
    color: var(--ink-white); font-size: 12.5px; line-height: 1.35;
  }
  .person-name { font-size: 19px; font-weight: 700; letter-spacing: 1px; text-transform: uppercase; }
  .person-role { font-size: 12px; margin-bottom: 10px; }
  .address { margin-bottom: 10px; }
  .licence { margin-top: 6px; font-size: 11px; }
  .front-brand {
    position: absolute; right: 26px; bottom: 30px;
    display: flex; align-items: center; gap: 12px; color: var(--ink-white);
  }
  .front-brand .brand-dot { background: var(--ink-white); width: 40px; height: 40px; }
  .front-name { font-weight: 700; font-size: 29px; line-height: 1; text-transform: uppercase; letter-spacing: 1px; }
  .front-tagline { font-size: 10.5px; font-weight: 600; margin-top: 4px; }
</style>
</head>
<body>

  <section class="card card-reverse">
    <div class="reverse-brand">
      <span class="brand-dot"></span>
      <span class="reverse-name">Brightmoor Paving</span>
    </div>
    <p class="reverse-tagline">Synthetic Grass &amp; Softfall Rubber Surfaces</p>
    <p class="service-list">
      <span class="service-blue">Synthetic Grass</span><span class="service-sep">|</span>
      <span class="service-green">Wetpour Rubber Surfaces</span><span class="service-sep">|</span>
      <span class="service-blue">Softfall Surfaces</span><br>
      <span class="service-green">Rubber Wood Mulch</span><span class="service-sep">|</span>
      <span class="service-blue">Shade Structures</span><span class="service-sep">|</span>
      <span class="service-green">Landscape Structures</span>
    </p>
  </section>

  <section class="card card-front">
    <svg class="front-split" width="540" height="330" viewBox="0 0 540 330" aria-hidden="true">
      <defs>
        <linearGradient id="greenPanel" x1="0" y1="0" x2="1" y2="1">
          <stop offset="0" stop-color="#8dcc4e"/>
          <stop offset="1" stop-color="#6cb536"/>
        </linearGradient>
      </defs>
      <path d="M230 0 C 170 80, 200 160, 215 230 C 225 280, 215 310, 222 330 L540 330 L540 0 Z" fill="url(#greenPanel)"/>
      <path d="M230 0 C 170 80, 200 160, 215 230 C 225 280, 215 310, 222 330" fill="none" stroke="#1a1a1a" stroke-width="4"/>
    </svg>

    <div class="contact-block">
      <p class="person-name">Dana Whitfield</p>
      <p class="person-role">Managing Director</p>
      <p class="address">Riverton City, Eastvale,<br>P.O. Box 000000</p>
      <p>P: +00 21 480 000&nbsp;&nbsp;F: +00 21 480 000</p>
      <p>E: info@brightmoorpaving.com</p>
      <p>W: www.brightmoorpaving.com</p>
      <p class="licence">Trade Licence #4410962</p>
    </div>

    <div class="front-brand">
      <span class="brand-dot"></span>
      <div>
        <p class="front-name">Brightmoor<br>Paving</p>
        <p class="front-tagline">Synthetic Grass &amp; Softfall Rubber Surfaces</p>
      </div>
    </div>
  </section>

</body>
</html>
```